Single-sided business card for restaurant bellwether with new logo made on this site

Business card options with new logo including restaurant name, address, phone number and website. This business card is single-sided only and will be presented at the hostess desk for clients to take. I would like to see options based on a cream card background, a white card background, a yellow card background and a burgundy colored background. It needs to be elegant and traditional.

Target Market(s)

local and international crowd

Industry/Entity Type

restaurant

Contact Information for Business Card

address, website and phone number

Font styles to use
Serif

Colors
EE7325
F08F49
F5BC92
FAE3D3
FDF4ED

Requirements
Must have
• new logo, address, phone number, website
Should not have
• more than three colors

```html
<!DOCTYPE html>
<html lang="es">
<head>
<meta charset="utf-8">
<title>Bellwether — tarjetas de presentación</title>
<link rel="stylesheet" href="https://fonts.googleapis.com/css2?family=Open+Sans:wght@400;600&display=swap">
<style>
  :root {
    --backdrop: #7d7d7d;
    --burgundy: #3f1e1e;
    --gold: #f2b535;
    --yellow: #f7c15a;
    --cocoa: #3d1f1c;
    --white: #ffffff;
  }
  * { box-sizing: border-box; margin: 0; padding: 0; }
  html, body {
    width: 1200px; height: 1002px; overflow: hidden;
    background: var(--backdrop);
    font-family: "Open Sans", sans-serif;
  }
  .stage { position: relative; width: 1200px; height: 1002px; }
  .card {
    position: absolute; top: 207px; width: 397px; height: 695px;
  }
  .card--burgundy { left: 144px; background: var(--burgundy); --ink: var(--white); --accent: var(--gold); }
  .card--yellow { left: 650px; background: var(--yellow); --ink: var(--cocoa); --accent: var(--cocoa); }
  .card__frame {
    position: absolute; inset: 18px;
    border: 2.5px solid var(--accent);
  }
  .brand {
    position: absolute; top: 89px; left: 0; right: 0;
    display: flex; flex-direction: column; align-items: center;
  }
  .brand__square {
    width: 142px; height: 142px; background: var(--accent);
  }
  .card--burgundy .brand__square { background: var(--gold); }
  .brand__name {
    margin-top: 44px;
    font-size: 29px; font-weight: 400; letter-spacing: 0.14em;
    color: var(--ink); text-transform: uppercase;
  }
  .address {
    position: absolute; top: 405px; left: 0; right: 0;
    text-align: center; font-size: 17px; line-height: 26px; color: var(--ink);
  }
  .address__title { color: var(--accent); }
  .card--yellow .address__title { font-weight: 600; }
  .contact-divider {
    position: absolute; top: 541px; left: 0; right: 0;
    display: flex; justify-content: center; align-items: center; gap: 8px;
  }
  .contact-divider__rule { width: 66px; height: 2px; background: var(--accent); margin: 0 6px; }
  .contact-divider svg { width: 23px; height: 23px; display: block; }
  .contact {
    position: absolute; top: 594px; left: 0; right: 0;
    text-align: center; font-size: 17px; line-height: 26px; color: var(--ink);
  }
</style>
</head>
<body>
<main class="stage">

  <section class="card card--burgundy" aria-label="Tarjeta burdeos">
    <div class="card__frame"></div>
    <div class="brand">
      <div class="brand__square"></div>
      <div class="brand__name">Bellwether</div>
    </div>
    <p class="address">
      <span class="address__title">Restaurant Bellwether</span><br>
      Alameda 415<br>
      Bahía Serena, Oaxaca CP 70900
    </p>
    <div class="contact-divider">
      <span class="contact-divider__rule"></span>
      <svg viewBox="0 0 24 24" aria-label="Teléfono"><circle cx="12" cy="12" r="12" fill="#f2b535"/><path d="M8 6.5c.6-.4 1.3-.3 1.7.3l1.1 1.8c.3.5.2 1.1-.2 1.5l-.8.7c.6 1.4 1.7 2.6 3.1 3.2l.7-.8c.4-.4 1-.5 1.5-.2l1.8 1.1c.6.4.7 1.1.3 1.7l-.7.9c-.6.7-1.6.9-2.5.5-3.2-1.4-5.6-3.9-6.9-7.1-.3-.9-.1-1.9.6-2.5z" fill="#3f1e1e"/></svg>
      <svg viewBox="0 0 24 24" aria-label="Sitio web"><circle cx="12" cy="12" r="12" fill="#f2b535"/><g fill="none" stroke="#3f1e1e" stroke-width="1.1"><circle cx="12" cy="12" r="6"/><ellipse cx="12" cy="12" rx="2.6" ry="6"/><path d="M6 12h12M7 9h10M7 15h10"/></g></svg>
      <span class="contact-divider__rule"></span>
    </div>
    <p class="contact">958-555-0142<br>www.bellwether.com.mx</p>
  </section>

  <section class="card card--yellow" aria-label="Tarjeta amarilla">
    <div class="card__frame"></div>
    <div class="brand">
      <div class="brand__square"></div>
      <div class="brand__name">Bellwether</div>
    </div>
    <p class="address">
      <span class="address__title">Restaurant Bellwether</span><br>
      Alameda 415<br>
      Bahía Serena, Oaxaca CP 70900
    </p>
    <div class="contact-divider">
      <span class="contact-divider__rule"></span>
      <svg viewBox="0 0 24 24" aria-label="Teléfono"><circle cx="12" cy="12" r="12" fill="#3d1f1c"/><path d="M8 6.5c.6-.4 1.3-.3 1.7.3l1.1 1.8c.3.5.2 1.1-.2 1.5l-.8.7c.6 1.4 1.7 2.6 3.1 3.2l.7-.8c.4-.4 1-.5 1.5-.2l1.8 1.1c.6.4.7 1.1.3 1.7l-.7.9c-.6.7-1.6.9-2.5.5-3.2-1.4-5.6-3.9-6.9-7.1-.3-.9-.1-1.9.6-2.5z" fill="#f7c15a"/></svg>
      <svg viewBox="0 0 24 24" aria-label="Sitio web"><circle cx="12" cy="12" r="12" fill="#3d1f1c"/><g fill="none" stroke="#f7c15a" stroke-width="1.1"><circle cx="12" cy="12" r="6"/><ellipse cx="12" cy="12" rx="2.6" ry="6"/><path d="M6 12h12M7 9h10M7 15h10"/></g></svg>
      <span class="contact-divider__rule"></span>
    </div>
    <p class="contact">958-555-0142<br>www.bellwether.com.mx</p>
  </section>

</main>
</body>
</html>
```